Criação de Cartao de Visita para Computador & Internet
" Nossos clientes fazem o outsorcing da TI para nós, assim cuidamos de todos os recursos se serviços de TI, também vendemos hardwares e softwares "

```html
<!DOCTYPE html>
<html lang="pt-BR">
<head>
<meta charset="utf-8">
<title>Nexa Corp — Cartão de Visita</title>
<link rel="stylesheet" href="https://fonts.googleapis.com/css2?family=Open+Sans:ital,wght@0,300;0,400;0,600;0,700;1,400&display=swap">
<style>
  :root{
    --bg:#e9ecef;
    --white:#ffffff;
    --paper-gray:#eef1f4;
    --blue-dark:#0f5d8f;
    --blue:#1f7fbf;
    --blue-light:#4aa6db;
    --text-dark:#23506f;
    --text-light:#ffffff;
    --rule:#9fc3dc;
  }
  *{box-sizing:border-box;margin:0;padding:0}
  html,body{width:1200px;height:1200px;overflow:hidden}
  body{background:var(--bg);font-family:"Open Sans",Arial,sans-serif;position:relative}

  .card{position:absolute;background:var(--white);border-radius:18px;overflow:hidden;
        box-shadow:0 10px 30px rgba(0,0,0,.18)}
  .card__shape{position:absolute;inset:0;width:100%;height:100%}

  /* Front (vertical) */
  .card--front{left:70px;top:250px;width:400px;height:700px}
  .brand{position:absolute;left:0;right:0;top:120px;display:flex;align-items:center;justify-content:center;gap:16px}
  .brand__dot{width:30px;height:30px;border-radius:50%;background:var(--blue)}
  .brand__name{font-weight:700;font-size:46px;color:var(--blue);letter-spacing:.5px}

  .person{position:absolute;left:150px;top:380px;color:var(--text-light)}
  .person__name{font-weight:300;font-size:32px;line-height:1.1}
  .person__role{font-weight:700;font-size:15px;margin-top:4px}
  .person__division{font-weight:700;font-size:14px;margin-top:2px;text-transform:uppercase;letter-spacing:.4px}

  .contacts{position:absolute;left:96px;top:490px;list-style:none;color:var(--text-light);font-size:12.5px}
  .contacts li{display:flex;align-items:center;gap:12px;margin-bottom:12px;line-height:1.3}
  .contacts svg{width:22px;height:22px;flex:none}

  /* Back (horizontal) */
  .card--back{left:510px;top:250px;width:620px;height:354px}
  .division{position:absolute;top:46px;color:var(--text-dark)}
  .division--it{left:40px;width:255px}
  .division--events{left:330px;width:250px}
  .division__title{font-weight:700;font-size:18px;color:var(--blue-dark)}
  .division__subtitle{font-weight:600;font-size:13px;color:var(--blue-dark);margin-bottom:14px}
  .services{list-style:none;font-size:13px;line-height:1.45}
  .services li{position:relative;padding-left:14px;margin-bottom:3px}
  .services li::before{content:"";position:absolute;left:0;top:8px;width:5px;height:5px;border-radius:50%;background:var(--blue)}
  .divider{position:absolute;left:310px;top:50px;width:1px;height:200px;background:var(--rule)}
</style>
</head>
<body>

  <section class="card card--front" aria-label="Frente do cartão">
    <svg class="card__shape" viewBox="0 0 400 700" preserveAspectRatio="none" aria-hidden="true">
      <defs>
        <linearGradient id="frontBlue" x1="0" y1="0" x2="1" y2="1">
          <stop offset="0" stop-color="#2b8fcf"/>
          <stop offset="1" stop-color="#0f5d8f"/>
        </linearGradient>
      </defs>
      <rect width="400" height="700" fill="#ffffff"/>
      <path d="M0 330 C120 300 150 250 260 260 C330 266 370 250 400 230 L400 700 L0 700 Z" fill="#bcdcf0"/>
      <path d="M0 350 C120 320 160 275 270 282 C335 286 375 270 400 252 L400 700 L0 700 Z" fill="url(#frontBlue)"/>
      <path d="M0 610 C120 580 260 640 400 600 L400 700 L0 700 Z" fill="#0b4f7b" opacity=".45"/>
    </svg>

    <div class="brand">
      <span class="brand__dot"></span>
      <span class="brand__name">Nexa Corp</span>
    </div>

    <div class="person">
      <p class="person__name">Marina Toledo</p>
      <p class="person__role">Diretora Executiva</p>
      <p class="person__division">Divisão de Eventos</p>
    </div>

    <ul class="contacts">
      <li>
        <svg viewBox="0 0 24 24"><circle cx="12" cy="12" r="11" fill="#fff"/><path d="M8.2 6.5l2 2.3-1 1.4c.7 1.6 1.9 2.8 3.5 3.6l1.4-1 2.3 2-1.2 1.7c-3.9-.5-7.3-3.9-7.8-7.8z" fill="#1f7fbf"/></svg>
        <span>(11) 4002-1830 (São Paulo)<br>0800 725 4410 (Demais localidades)</span>
      </li>
      <li>
        <svg viewBox="0 0 24 24"><circle cx="12" cy="12" r="11" fill="#fff"/><rect x="9" y="6" width="6" height="12" rx="1.2" fill="#1f7fbf"/></svg>
        <span>(11) 98741-2206</span>
      </li>
      <li>
        <svg viewBox="0 0 24 24"><circle cx="12" cy="12" r="11" fill="#fff"/><rect x="6.5" y="8" width="11" height="8" rx="1" fill="#1f7fbf"/><path d="M6.8 8.5l5.2 4 5.2-4" stroke="#fff" stroke-width="1.2" fill="none"/></svg>
        <span>marina.toledo@nexacorp.com.br</span>
      </li>
      <li>
        <svg viewBox="0 0 24 24"><circle cx="12" cy="12" r="11" fill="#fff"/><circle cx="12" cy="12" r="6" fill="none" stroke="#1f7fbf" stroke-width="1.4"/><path d="M6 12h12M12 6c-2.5 3-2.5 9 0 12M12 6c2.5 3 2.5 9 0 12" stroke="#1f7fbf" stroke-width="1.2" fill="none"/></svg>
        <span>www.nexacorp.com.br</span>
      </li>
    </ul>
  </section>

  <section class="card card--back" aria-label="Verso do cartão">
    <svg class="card__shape" viewBox="0 0 620 354" preserveAspectRatio="none" aria-hidden="true">
      <rect width="620" height="354" fill="#ffffff"/>
      <path d="M0 300 C180 280 360 330 620 270 L620 354 L0 354 Z" fill="#bcdcf0"/>
      <path d="M0 318 C180 300 380 345 620 292 L620 354 L0 354 Z" fill="#1f7fbf"/>
    </svg>

    <div class="division division--it">
      <h2 class="division__title">Divisão de TI</h2>
      <p class="division__subtitle">Soluções em Tecnologia da Informação</p>
      <ul class="services">
        <li>Administração e Suporte de TI (Outsourcing)</li>
        <li>Locação e Venda de Hardware e Software</li>
        <li>Cloud Solutions</li>
        <li>Consultoria e Projetos de TI</li>
        <li>Segurança e Proteção de Dados</li>
      </ul>
    </div>

    <span class="divider"></span>

    <div class="division division--events">
      <h2 class="division__title">Divisão de Eventos</h2>
      <p class="division__subtitle">Soluções para Gestão Jurídica</p>
      <ul class="services">
        <li>Coquetéis</li>
        <li>Seminários</li>
        <li>Congressos</li>
        <li>Cursos</li>
        <li>Workshop</li>
        <li>Networking</li>
        <li>Conexões Empresariais</li>
      </ul>
    </div>
  </section>

</body>
</html>
```